FotoVELTA buisnesscard

Hey :) I need a modern buisnesscard for my company FotoVELTA
It most have:
Dagligleder og Fotograf: Henrik Torvald Bjelland

Mob: +4791642058
Epost: post@fotovelta.no
Adresse: Bakkestien22, 6087 Fjellvik

Facbook and instagram logo with text FotoVELTA

FotoVELTA logo

It Company

```html
<!DOCTYPE html>
<html lang="no">
<head>
<meta charset="utf-8">
<title>FotoVELTA – visittkort</title>
<link rel="stylesheet" href="https://fonts.googleapis.com/css2?family=Barlow:wght@400;500;600&display=swap">
<style>
  :root {
    --page: #ffffff;
    --card-dark: #141414;
    --card-mid: #3a3a3a;
    --facet-a: #2b2b2b;
    --facet-b: #444444;
    --facet-c: #1e1e1e;
    --text-light: #f2f2f2;
    --accent-blue: #86cfe8;
    --icon-glyph: #1b1b1b;
  }
  * { box-sizing: border-box; margin: 0; padding: 0; }
  html, body { width: 1200px; height: 1200px; overflow: hidden; background: var(--page); }
  body { position: relative; font-family: "Barlow", Arial, sans-serif; }

  .card {
    position: absolute;
    left: 218px;
    width: 731px;
    height: 472px;
    overflow: hidden;
    box-shadow: 0 4px 14px rgba(0,0,0,0.35);
  }
  .card--front {
    top: 94px;
    background: radial-gradient(ellipse at 50% 40%, var(--card-mid) 0%, var(--card-dark) 75%);
  }
  .card--back {
    top: 624px;
    background: radial-gradient(ellipse at 62% 30%, var(--card-mid) 0%, var(--card-dark) 80%);
  }
  .card__facets { position: absolute; inset: 0; width: 100%; height: 100%; }

  .front-name {
    position: absolute;
    left: 0; right: 0;
    top: 272px;
    line-height: 84px;
    text-align: center;
    font-weight: 600;
    font-size: 68px;
    letter-spacing: 1px;
    color: var(--accent-blue);
  }

  .back-name {
    position: absolute;
    left: 0; right: 0;
    top: 60px;
    text-align: center;
    font-weight: 600;
    font-size: 44px;
    color: var(--text-light);
  }
  .person {
    position: absolute;
    left: 0; right: 0;
    top: 188px;
    text-align: center;
  }
  .person__name {
    font-weight: 600;
    font-size: 31px;
    color: var(--text-light);
    letter-spacing: 0.5px;
  }
  .person__role {
    margin-top: 6px;
    font-weight: 400;
    font-size: 26px;
    color: var(--accent-blue);
    letter-spacing: 2px;
  }

  .contacts {
    position: absolute;
    left: 31px;
    top: 336px;
    list-style: none;
  }
  .contacts__item {
    display: flex;
    align-items: center;
    height: 37px;
    font-size: 21px;
    color: var(--text-light);
    letter-spacing: 1px;
  }
  .icon { width: 26px; height: 26px; margin-right: 9px; flex: none; }

  .social {
    position: absolute;
    left: 518px;
    top: 413px;
    height: 30px;
    display: flex;
    align-items: center;
    font-size: 23px;
    color: var(--text-light);
    letter-spacing: 2px;
  }
  .social__dot {
    width: 26px; height: 26px;
    border-radius: 50%;
    background: var(--accent-blue);
    margin-right: 10px;
  }
</style>
</head>
<body>

<section class="card card--front" aria-label="Forside">
  <svg class="card__facets" viewBox="0 0 731 472" aria-hidden="true">
    <polygon points="380,0 731,0 731,180" fill="var(--facet-a)"/>
    <polygon points="480,0 731,0 731,90 600,0" fill="var(--facet-b)" opacity="0.6"/>
    <polygon points="560,0 731,0 731,50" fill="var(--facet-c)"/>
    <polygon points="0,250 0,472 220,472" fill="var(--facet-a)"/>
    <polygon points="0,330 0,472 130,472" fill="var(--facet-b)" opacity="0.6"/>
    <polygon points="0,400 0,472 60,472" fill="var(--facet-c)"/>
  </svg>
  <div class="front-name">FotoVELTA</div>
</section>

<section class="card card--back" aria-label="Bakside">
  <div class="back-name">FotoVELTA</div>

  <div class="person">
    <div class="person__name">Henrik Torvald Bjelland</div>
    <div class="person__role">Dagligleder og Fotograf</div>
  </div>

  <ul class="contacts">
    <li class="contacts__item">
      <svg class="icon" viewBox="0 0 26 26" aria-hidden="true">
        <circle cx="13" cy="13" r="13" fill="var(--accent-blue)"/>
        <path d="M8.5 7.5c.8-.8 1.7-.7 2.2.1l1 1.6c.4.7.2 1.3-.4 1.8l-.6.5c.6 1.4 1.6 2.4 3 3l.5-.6c.5-.6 1.1-.8 1.8-.4l1.6 1c.8.5.9 1.4.1 2.2-1 1-2.4 1.3-3.8.6-2.6-1.2-4.6-3.2-5.8-5.8-.7-1.4-.4-2.8.4-4z" fill="var(--icon-glyph)"/>
      </svg>
      +4791642058
    </li>
    <li class="contacts__item">
      <svg class="icon" viewBox="0 0 26 26" aria-hidden="true">
        <circle cx="13" cy="13" r="13" fill="var(--accent-blue)"/>
        <rect x="6.5" y="8.5" width="13" height="9" rx="1" fill="var(--icon-glyph)"/>
        <path d="M7 9.2l6 4.6 6-4.6" fill="none" stroke="var(--accent-blue)" stroke-width="1.3"/>
      </svg>
      post@fotovelta.no
    </li>
    <li class="contacts__item">
      <svg class="icon" viewBox="0 0 26 26" aria-hidden="true">
        <circle cx="13" cy="13" r="13" fill="var(--accent-blue)"/>
        <path d="M13 5.5c-3 0-5.2 2.2-5.2 5.1 0 3.7 5.2 9.6 5.2 9.6s5.2-5.9 5.2-9.6c0-2.9-2.2-5.1-5.2-5.1z" fill="var(--icon-glyph)"/>
        <circle cx="13" cy="10.6" r="2" fill="var(--accent-blue)"/>
      </svg>
      Bakkestien22, 6087 Fjellvik
    </li>
  </ul>

  <div class="social">
    <span class="social__dot" aria-hidden="true"></span>
    FotoVELTA
  </div>
</section>

</body>
</html>
```